Publisher needs a book cover design for ‘Lanterns Over the Marsh Gate’ book

We need a book cover (front, back, spine) for the 2nd edition of a book entitled ‘Lanterns Over the Marsh Gate’ and subtitled ‘the quiet geography of tidal winds, ferry routes and harbour lanterns’ (inverted commas not to be part of the title and subtitle). The author is Rupert Calloway. The publisher is Vellmark Press. The finished size of the paperback version will be the industry standard 9" x 6". There will be paperback, hardback, and e-book versions. The final number of pages is expected to be in the region 150-180 pages. Text for the back cover is not yet available, but at the bottom of the back cover should be publisher logo (rectangular) on the left and space for the ISBN bar code on the right. The circular logo should be on the spine. The design should be original and not include any stock images that have been created by someone else or may require obtaining a copyright licence to use. Symbols in common use and not copyrighted are probably ok. There are no required images, photographs or symbols except the publisher logo at the left bottom of the back cover and lower spine. Spine lettering should be UK/US style with the top of the writing nearest the front cover. The designer is free to be creative using appropriate diagrams, symbols or abstract designs. Rectangular and circular variants of the publisher logo are attached. Designers are assured that when evaluating designs absolutely no notice whatsoever is taken of a designer's Pixo Rally ranking or status; We are completely output driven, so what matters is the design, not the ranking or status of the designer. In a similar way, designs are not evaluated as 'good' or 'bad' - the winning design will be chosen after review by a design review panel and is not decided arbitrarily by a single person. All submitted designs should be capable of effective copyright assignment.

Target Market(s)

Practitioners, parents, teachers, pupils and academics concerned with child protection, safeguarding and the elimination of emotional abuse of children in the classroom

Font styles to use
Serif
Sans Serif

Requirements
Must have
• • Title, author, edition, subtitle, publisher logo
Nice to have
• • Originality, innovation
Should not have
• • Stock images or anything else requiring additional copyright discussions and negotiations.

```html
<!DOCTYPE html>
<html lang="en">
<head>
<meta charset="utf-8">
<title>Lanterns Over the Marsh Gate — Cover Wrap</title>
<link rel="stylesheet" href="https://fonts.googleapis.com/css2?family=Anton&family=Oswald:wght@500&family=Roboto+Condensed:wght@500&family=Roboto:wght@400&display=swap">
<style>
  :root {
    --navy-deep: #020a3c;
    --navy-mid: #0a1a9a;
    --blue-glow: #1f36d6;
    --white: #ffffff;
    --sun: #f2cb4a;
    --teal: #44e2c6;
    --coral: #f26b5b;
    --ink-box: #ffffff;
  }
  * { margin: 0; padding: 0; box-sizing: border-box; }
  html, body { width: 1200px; height: 859px; overflow: hidden; background: var(--navy-deep); }
  .cover-wrap {
    position: relative;
    width: 1200px; height: 859px;
    background:
      radial-gradient(ellipse 360px 420px at 300px 430px, var(--blue-glow) 0%, rgba(31,54,214,0) 100%),
      radial-gradient(ellipse 420px 460px at 900px 400px, var(--navy-mid) 0%, rgba(10,26,154,0) 100%),
      var(--navy-deep);
    color: var(--white);
    overflow: hidden;
  }

  /* Back cover */
  .back-title {
    position: absolute; left: 90px; top: 140px;
    font-family: "Oswald", sans-serif; font-weight: 500;
    font-size: 33px; line-height: 40px; letter-spacing: -0.3px;
    text-transform: uppercase; white-space: nowrap;
    transform: scaleX(0.88); transform-origin: left top;
  }
  .back-blurb {
    position: absolute; left: 90px; top: 253px; width: 400px;
    font-family: "Roboto Condensed", sans-serif; font-weight: 500;
    font-size: 14.2px; line-height: 19.2px; white-space: nowrap;
  }
  .publisher-mark {
    position: absolute; left: 34px; top: 764px;
    display: flex; align-items: center; gap: 10px;
  }
  .publisher-mark .dot {
    width: 60px; height: 60px; border-radius: 50%; background: var(--white);
  }
  .publisher-mark .name {
    font-family: "Oswald", sans-serif; font-weight: 500;
    font-size: 34px; letter-spacing: 1px; text-transform: uppercase;
  }
  .isbn-space {
    position: absolute; left: 370px; top: 718px; width: 183px; height: 118px;
    background: var(--ink-box);
  }

  /* Spine */
  .spine-title, .spine-author {
    position: absolute; left: 612px;
    font-family: "Anton", sans-serif; font-size: 22px; line-height: 24px;
    text-transform: uppercase; white-space: nowrap;
    transform: rotate(90deg); transform-origin: left top;
  }
  .spine-title { top: 38px; letter-spacing: 0.2px; }
  .spine-author { top: 606px; }
  .spine-mark {
    position: absolute; left: 585px; top: 802px;
    display: flex; flex-direction: column; align-items: center; gap: 2px;
    width: 30px;
  }
  .spine-mark .dot { width: 20px; height: 20px; border-radius: 50%; background: var(--white); }
  .spine-mark .name {
    font-family: "Oswald", sans-serif; font-weight: 500; font-size: 6px; letter-spacing: 0.3px;
    text-transform: uppercase;
  }

  /* Front cover */
  .front-title { position: absolute; left: 0; top: 0; }
  .front-title text { font-family: "Anton", sans-serif; text-transform: uppercase; }
  .front-subtitle {
    position: absolute; left: 662px; top: 441px; width: 500px;
    font-family: "Roboto", sans-serif; font-weight: 400;
    font-size: 17.4px; line-height: 22.4px; text-align: center;
    text-transform: uppercase; letter-spacing: 0.2px;
  }
  .front-art {
    position: absolute; left: 824px; top: 494px; width: 176px; height: 270px;
    background: linear-gradient(180deg, var(--teal) 0%, var(--teal) 50%, var(--coral) 62%, var(--coral) 100%);
  }
  .front-author {
    position: absolute; left: 798px; top: 790px; width: 238px;
    font-family: "Anton", sans-serif; font-size: 38px; line-height: 46px;
    text-transform: uppercase; text-align: center; white-space: nowrap;
    transform: scaleX(0.8); transform-origin: center top;
  }
</style>
</head>
<body>
<main class="cover-wrap">

  <section class="back-cover">
    <h2 class="back-title">Lanterns Over the Marsh Gate</h2>
    <p class="back-blurb">
      Sed ut perspiciatis unde omnis iste natus error sit voluptatem<br>
      accusantium doloremque laudantium, totam rem aperiam, eaque<br>
      ipsa quae ab illo inventore veritatis et quasi architecto beatae<br>
      vitae dicta sunt explicabo. Nemo enim ipsam voluptatem quia<br>
      voluptas sit aspernatur aut odit aut fugit, sed quia consequuntur<br>
      magni dolores eos qui ratione voluptatem sequi nesciunt. Neque<br>
      porro quisquam est, qui dolorem ipsum quia dolor sit amet,<br>
      consectetur, adipisci velit, sed quia non numquam eius modi<br>
      tempora incidunt ut labore et dolore magnam aliquam quaerat<br>
      voluptatem. Ut enim ad minima veniam, quis nostrum<br>
      exercitationem ullam corporis suscipit laboriosam, nisi ut aliquid<br>
      ex ea commodi consequatur? Quis autem vel eum iure<br>
      reprehenderit qui in ea voluptate velit esse quam nihil molestiae<br>
      consequatur, vel illum qui dolorem eum fugiat quo voluptas nulla<br>
      pariatur
    </p>
    <div class="publisher-mark">
      <span class="dot"></span>
      <span class="name">Vellmark Press</span>
    </div>
    <div class="isbn-space"></div>
  </section>

  <section class="spine">
    <div class="spine-title">Lanterns Over the Marsh Gate</div>
    <div class="spine-author">Rupert Calloway</div>
    <div class="spine-mark">
      <span class="dot"></span>
      <span class="name">Vellmark</span>
    </div>
  </section>

  <section class="front-cover">
    <svg class="front-title" width="1200" height="430" viewBox="0 0 1200 430" aria-label="Lanterns Over the Marsh Gate">
      <text x="661" y="160" font-size="142" fill="var(--white)" textLength="497" lengthAdjust="spacingAndGlyphs">Lanterns</text>
      <text x="659" y="339" font-size="202" fill="var(--sun)" textLength="499" lengthAdjust="spacingAndGlyphs">Over the</text>
      <text x="662" y="418" font-size="84" fill="var(--white)" textLength="496" lengthAdjust="spacingAndGlyphs">Marsh Gate</text>
    </svg>
    <p class="front-subtitle">The quiet geography of tidal winds,<br>ferry routes and harbour lanterns.</p>
    <div class="front-art" role="img" aria-label="Flat illustration of a lone figure sitting hunched in the corner of a teal-walled room on a coral floor"></div>
    <div class="front-author">Rupert Calloway</div>
  </section>

</main>
</body>
</html>
```